Vantor Scorecard

Redesign KLT's existing Vantor scorecard, which tracks and reports key performance indicators (KPIs) for our clients. The scorecard provides our customers with an at-a-glance view of our on-site performance. Vantor is a tool that automatically populates and reports this data.

Review the attached document and deliver suggested redesign options for the two attached views.
Page 1: Portfolio-wide views (high level rollup of multiple sites)
Page 2: Site-level view
Updates

Project Deadline Extended
Reason: Due to the holiday season within the U.S. around the globe we have decided to extend out deadline in hopes of gaining more participation. We will also be providing comments to the current designs tomorrow.

Font styles to use
Sans Serif

Requirements
Must have
• - Sans serif fonts
- Clean aesthetic
- Utilize the exact key performance indicators as are in the attached mockup
- White background (think Plum-esque)
Nice to have
• - Ideas for animation of design elements
Should not have
• - Pictures (icons are okay)

```html
<!DOCTYPE html>
<html lang="en">
<head>
<meta charset="utf-8">
<title>Tallix Scorecard – All Sites</title>
<link href="https://fonts.googleapis.com/css2?family=Open+Sans:wght@300;400;600;700&display=swap" rel="stylesheet">
<style>
:root{
  --orange:#ee8a00;
  --orange-dark:#b06a00;
  --green:#6ea516;
  --green-dark:#4e7a0c;
  --ink:#444;
  --ink-soft:#666;
  --grey-line:#7a7a7a;
  --grid:#dcdcdc;
  --paper:#fff;
}
*{margin:0;padding:0;box-sizing:border-box}
html,body{width:1200px;height:996px;overflow:hidden;background:var(--paper)}
body{position:relative;font-family:"Open Sans",Arial,sans-serif;color:var(--ink)}
.band{position:absolute;left:0;width:1200px;background:var(--paper)}
.band--header{top:0;height:135px;box-shadow:0 10px 18px -8px rgba(0,0,0,.18);z-index:2}
.band--nav{top:135px;height:240px;box-shadow:0 12px 18px -10px rgba(0,0,0,.16);z-index:1}
.brand{position:absolute;left:50px;top:44px;display:flex;align-items:center;gap:10px;font-size:30px;font-weight:600;color:#777}
.brand__dot{width:26px;height:26px;border-radius:50%;background:#777}
.page-title{position:absolute;left:283px;top:32px;font-size:43px;font-weight:400;color:var(--orange);line-height:1}
.page-sub{position:absolute;left:283px;top:84px;font-size:23px;color:var(--ink)}
.page-sub b{font-weight:700}
.product{position:absolute;left:952px;top:72px;font-size:42px;color:var(--orange);line-height:1}
.product small{font-size:24px;font-weight:600;color:var(--ink)}
.nav{position:absolute;top:41px;left:0;width:1200px}
.nav__item{position:absolute;width:120px;text-align:center;font-size:15px;font-weight:700;color:var(--ink)}
.nav__icon{display:block;margin:0 auto 8px;width:88px;height:88px;border-radius:50%;background:var(--orange)}
.tabs{position:absolute;top:174px;left:218px;display:flex;gap:6px}
.tab{width:136px;height:31px;line-height:31px;text-align:center;font-size:14px;font-weight:700;color:#fff;background:var(--green)}
.tab--active{background:var(--green-dark)}
.score-head{position:absolute;left:742px;top:405px}
.score-head h2{font-size:42px;font-weight:400;color:var(--orange);line-height:1.05}
.score-head .kpi{font-size:19px;font-weight:700;color:var(--ink);line-height:1.3}
.score-head .period{font-size:21px;color:var(--ink-soft);line-height:1.3}
.rule{position:absolute;left:736px;top:516px;width:464px;height:3px;background:var(--grey-line)}
.chart{position:absolute;left:0;top:500px}
.site-score{position:absolute;left:959px;top:540px}
.site-score h3{font-size:42px;font-weight:400;color:var(--orange);line-height:1.05}
.site-score p{font-size:19px;font-weight:700;color:var(--ink)}
.gauge{position:absolute;left:947px;top:631px;width:116px;height:116px;border-radius:50%;
  background:radial-gradient(circle at 50% 40%,#fafafa 0%,#e2e2e2 60%,#b8b8b8 100%);
  box-shadow:0 2px 4px rgba(0,0,0,.25);display:flex;align-items:center;justify-content:center;
  font-size:38px;font-weight:700;color:var(--green)}
.legend{position:absolute;left:125px;top:882px;width:785px;font-size:11.5px;line-height:16px;color:#333;text-align:justify;text-align-last:left}
</style>
</head>
<body>

<header class="band band--header">
  <div class="brand"><span class="brand__dot"></span>Corvane</div>
  <h1 class="page-title">All Sites</h1>
  <div class="page-sub"><b>All Programs |</b> July 2013</div>
  <div class="product">KLT<small>Tallix</small></div>
</header>

<nav class="band band--nav">
  <div class="nav">
    <div class="nav__item" style="left:207px">
      <svg class="nav__icon" viewBox="0 0 88 88" aria-hidden="true">
        <circle cx="44" cy="44" r="44" fill="#b06a00"/>
        <g fill="none" stroke="#fff" stroke-width="2">
          <rect x="37" y="26" width="14" height="10"/><rect x="20" y="48" width="14" height="10"/><rect x="54" y="48" width="14" height="10"/>
          <path d="M44 36v17M34 53h20" stroke-dasharray="2 2"/>
        </g>
      </svg>Governance</div>
    <div class="nav__item" style="left:345px">
      <svg class="nav__icon" viewBox="0 0 88 88" aria-hidden="true">
        <circle cx="44" cy="44" r="44" fill="#ee8a00"/>
        <g fill="#fff"><rect x="28" y="50" width="6" height="12"/><rect x="37" y="44" width="6" height="18"/><rect x="46" y="48" width="6" height="14"/><rect x="55" y="38" width="6" height="24"/></g>
        <path d="M22 66h46M22 30v36M28 44l10-8 8 6 14-14" fill="none" stroke="#fff" stroke-width="2"/>
      </svg>Cost</div>
    <div class="nav__item" style="left:484px">
      <svg class="nav__icon" viewBox="0 0 88 88" aria-hidden="true">
        <circle cx="44" cy="44" r="44" fill="#ee8a00"/>
        <path d="M34 24h22l8 8v32H34z" fill="none" stroke="#fff" stroke-width="2.5"/>
        <path d="M44 36h14M44 42h14M44 48h14M44 54h14" stroke="#fff" stroke-width="2"/>
        <circle cx="32" cy="44" r="7" fill="#fff"/><path d="M28 50l-2 10 6-3 6 3-2-10" fill="#fff"/>
      </svg>Quality</div>
    <div class="nav__item" style="left:622px">
      <svg class="nav__icon" viewBox="0 0 88 88" aria-hidden="true">
        <circle cx="44" cy="44" r="44" fill="#ee8a00"/>
        <circle cx="44" cy="34" r="10" fill="#fff"/>
        <path d="M26 66c0-12 8-18 18-18s18 6 18 18z" fill="#fff"/>
        <path d="M44 48l-3 6 3 10 3-10z" fill="#ee8a00"/>
      </svg>EHS</div>
    <div class="nav__item" style="left:760px">
      <svg class="nav__icon" viewBox="0 0 88 88" aria-hidden="true">
        <circle cx="44" cy="44" r="44" fill="#ee8a00"/>
        <g fill="#fff"><circle cx="30" cy="36" r="7"/><circle cx="58" cy="36" r="7"/><circle cx="44" cy="40" r="9"/>
        <path d="M18 58c0-8 5-12 12-12s10 3 10 8v4z"/><path d="M70 58c0-8-5-12-12-12s-10 3-10 8v4z"/>
        <path d="M28 66c0-10 7-15 16-15s16 5 16 15z"/></g>
      </svg>Personnel</div>
    <div class="nav__item" style="left:899px">
      <svg class="nav__icon" viewBox="0 0 88 88" aria-hidden="true">
        <circle cx="44" cy="44" r="44" fill="#ee8a00"/>
        <path d="M30 24h24l6 6v34H30z" fill="none" stroke="#fff" stroke-width="2.5"/>
        <path d="M36 34h16M36 40h16M36 46h10" stroke="#fff" stroke-width="2"/>
        <path d="M50 66l4-12 12-14 4 4-12 14z" fill="#fff"/>
      </svg>Training</div>
  </div>
  <div class="tabs">
    <div class="tab tab--active">Scorecard/KPIs</div>
    <div class="tab">Updates</div>
    <div class="tab">Innovations</div>
  </div>
</nav>

<section class="score-head">
  <h2>Scorecard</h2>
  <div class="kpi">KPI Score By Site</div>
  <div class="period">Showing July 2013</div>
</section>
<div class="rule"></div>

<svg class="chart" width="940" height="370" viewBox="0 0 940 370" role="img" aria-label="Bar chart of KPI score by site, July 2013">
  <g stroke="var(--grid)" stroke-dasharray="2 2">
    <line x1="127" y1="46" x2="900" y2="46"/><line x1="127" y1="106" x2="900" y2="106"/>
    <line x1="127" y1="166" x2="900" y2="166"/><line x1="127" y1="226" x2="900" y2="226"/>
    <line x1="127" y1="286" x2="900" y2="286"/>
  </g>
  <g font-family="Open Sans, sans-serif" font-size="17" font-weight="700" fill="#555" text-anchor="end">
    <text x="115" y="52">100%</text><text x="115" y="112">90%</text><text x="115" y="172">80%</text>
    <text x="115" y="232">70%</text><text x="115" y="292">60%</text><text x="115" y="352">50%</text>
  </g>
  <g>
    <rect x="150" y="46" width="12" height="300" fill="var(--green)"/>
    <rect x="177.2" y="112" width="12" height="234" fill="var(--orange)"/>
    <rect x="204.4" y="124" width="12" height="222" fill="var(--green)"/>
    <rect x="231.6" y="46" width="12" height="300" fill="var(--orange)"/>
    <rect x="258.8" y="82" width="12" height="264" fill="var(--green)"/>
    <rect x="286" y="106" width="12" height="240" fill="var(--orange)"/>
    <rect x="313.2" y="46" width="12" height="300" fill="var(--green)"/>
    <rect x="340.4" y="106" width="12" height="240" fill="var(--orange)"/>
    <rect x="367.6" y="124" width="12" height="222" fill="var(--green)"/>
    <rect x="394.8" y="46" width="12" height="300" fill="var(--orange)"/>
    <rect x="422" y="82" width="12" height="264" fill="var(--green)"/>
    <rect x="449.2" y="106" width="12" height="240" fill="var(--orange)"/>
    <rect x="476.4" y="46" width="12" height="300" fill="var(--green)"/>
    <rect x="503.6" y="82" width="12" height="264" fill="var(--orange)"/>
    <rect x="530.8" y="106" width="12" height="240" fill="var(--green)"/>
    <rect x="558" y="46" width="12" height="300" fill="var(--orange)"/>
    <rect x="585.2" y="106" width="12" height="240" fill="var(--green)"/>
    <rect x="612.4" y="127" width="12" height="219" fill="var(--orange)"/>
    <rect x="639.6" y="46" width="12" height="300" fill="var(--green)"/>
    <rect x="666.8" y="82" width="12" height="264" fill="var(--orange)"/>
    <rect x="694" y="106" width="12" height="240" fill="var(--green)"/>
    <rect x="721.2" y="106" width="12" height="240" fill="var(--orange)"/>
    <rect x="748.4" y="46" width="12" height="300" fill="var(--green)"/>
    <rect x="775.6" y="106" width="12" height="240" fill="var(--orange)"/>
    <rect x="802.8" y="46" width="12" height="300" fill="var(--green)"/>
    <rect x="830" y="46" width="12" height="300" fill="var(--orange)"/>
    <rect x="857.2" y="82" width="12" height="264" fill="var(--green)"/>
    <rect x="884.4" y="106" width="12" height="240" fill="var(--orange)"/>
  </g>
  <g stroke="#444" stroke-width="4">
    <line x1="127" y1="4" x2="127" y2="350"/><line x1="125" y1="350" x2="920" y2="350"/>
  </g>
  <g fill="#444">
    <circle cx="156" cy="346" r="8"/><circle cx="183.2" cy="346" r="8"/><circle cx="210.4" cy="346" r="8"/><circle cx="237.6" cy="346" r="8"/>
    <circle cx="264.8" cy="346" r="8"/><circle cx="292" cy="346" r="8"/><circle cx="319.2" cy="346" r="8"/><circle cx="346.4" cy="346" r="8"/>
    <circle cx="373.6" cy="346" r="8"/><circle cx="400.8" cy="346" r="8"/><circle cx="428" cy="346" r="8"/><circle cx="455.2" cy="346" r="8"/>
    <circle cx="482.4" cy="346" r="8"/><circle cx="509.6" cy="346" r="8"/><circle cx="536.8" cy="346" r="8"/><circle cx="564" cy="346" r="8"/>
    <circle cx="591.2" cy="346" r="8"/><circle cx="618.4" cy="346" r="8"/><circle cx="645.6" cy="346" r="8"/><circle cx="672.8" cy="346" r="8"/>
    <circle cx="700" cy="346" r="8"/><circle cx="727.2" cy="346" r="8"/><circle cx="754.4" cy="346" r="8"/><circle cx="781.6" cy="346" r="8"/>
    <circle cx="808.8" cy="346" r="8"/><circle cx="836" cy="346" r="8"/><circle cx="863.2" cy="346" r="8"/><circle cx="890.4" cy="346" r="8"/>
  </g>
  <g font-family="Open Sans, sans-serif" font-size="8.5" font-weight="700" fill="#fff" text-anchor="middle">
    <text x="156" y="349">1</text><text x="183.2" y="349">2</text><text x="210.4" y="349">3</text><text x="237.6" y="349">4</text>
    <text x="264.8" y="349">5</text><text x="292" y="349">6</text><text x="319.2" y="349">7</text><text x="346.4" y="349">8</text>
    <text x="373.6" y="349">9</text><text x="400.8" y="349">10</text><text x="428" y="349">11</text><text x="455.2" y="349">12</text>
    <text x="482.4" y="349">13</text><text x="509.6" y="349">14</text><text x="536.8" y="349">15</text><text x="564" y="349">16</text>
    <text x="591.2" y="349">17</text><text x="618.4" y="349">18</text><text x="645.6" y="349">19</text><text x="672.8" y="349">20</text>
    <text x="700" y="349">21</text><text x="727.2" y="349">22</text><text x="754.4" y="349">23</text><text x="781.6" y="349">24</text>
    <text x="808.8" y="349">25</text><text x="836" y="349">26</text><text x="863.2" y="349">27</text><text x="890.4" y="349">28</text>
  </g>
</svg>

<section class="site-score">
  <h3>Site Score</h3>
  <p>Goal 90%</p>
</section>
<div class="gauge">86%</div>

<p class="legend">1. Arclight - Ardel Park | 2. Ovara - Velmora | 3. BSQ - Torvale | 4. Little Nest - Bay Harbor | 5 QRX - Irwen Falls | 6. Hadley - San Lucan | 7. Homecare - Skellford | 8. Verdis - Bramwick | 9. Arclight - Ardel Park | 10 Ovara - Velmora | 11 BSQ - Torvale | 12. Little Nest - Bay Harbor | 13 QRX - Irwen Falls | 14. Hadley - San Lucan | 15. Homecare - Skellford | 16. Verdis - Bramwick | 17. Arclight - Ardel Park | 18. Ovara - Velmora | 19. BSQ - Torvale | 20. Little Nest - Bay Harbor | 22. QRX - Irwen Falls | 23. Hadley - San Lucan | 24. Homecare - Skellford | 25. Verdis - Bramwick | 26. Hadley - San Lucan | 27. Homecare - Skellford | 28. Verdis - Bramwick</p>

</body>
</html>
```